Meridel Haulage - Website

A clean, not cluttered informative website for our business. We specialize in the transportation of radioactive materials across North America. The site is mostly for information about our company and will not be used to attract business but will be used to attract employee's mainly drivers. Driver's are very hard to find in our area. One of the pages needs to be a job's posting page with an apply now button. Either an application can be filled out there or a resume can be uploaded which ever functionality works better. I would like a website that I can easily edit, ability to change text and photos.

Number of Pages Required

5+ page

Colors

Designer to choose colors to be used in the design.

Requirements
Must have
• Home - About - Services - Jobs - Contact pages
• A way prospective employee's can apply or upload their resume to be emailed to me
• Very clean apperance
Should not have
• I don't want it to be busy

```html
<!DOCTYPE html>
<html lang="en">
<head>
<meta charset="utf-8">
<title>Meridel Haulage</title>
<link rel="stylesheet" href="https://fonts.googleapis.com/css2?family=Roboto+Condensed:wght@400;700&family=Open+Sans:wght@400;600&family=Archivo+Black&display=swap">
<style>
:root{
  --red:#e1141f;
  --ink:#4a4a4a;
  --grey:#6b6b6b;
  --text:#666;
  --white:#fff;
  --hero-top:#6d6d6d;
  --hero-bottom:#3c3f44;
  --road:#2e3034;
  --band-top:#5d6168;
  --band-bottom:#72767c;
  --footer:#1f242c;
  --footer-line:#3a404a;
  --footer-text:#cfd3d8;
  --card-line:#ef6a71;
}
*{box-sizing:border-box;margin:0;padding:0}
html,body{width:1200px;height:3719px;overflow:hidden}
body{position:relative;background:var(--white);font-family:"Open Sans",Arial,sans-serif;color:var(--text)}
.abs{position:absolute}
.center-x{left:0;width:1200px;text-align:center}

/* header */
.site-header{top:0;left:0;width:1200px;height:119px;background:var(--white);z-index:5}
.brand{left:111px;top:34px;font-family:"Roboto Condensed",Arial,sans-serif;font-weight:700;font-size:40px;letter-spacing:1px;color:var(--red);text-transform:uppercase}
.main-nav a{position:absolute;top:52px;font-family:"Roboto Condensed",Arial,sans-serif;font-weight:700;font-size:15px;letter-spacing:.5px;color:var(--ink);text-decoration:none}
.main-nav a.active{color:var(--red)}

/* hero */
.hero{top:119px;left:0;width:1200px;height:700px;background:linear-gradient(180deg,var(--hero-top),#55585d 50%,var(--hero-bottom))}
.hero-title{top:345px;font-family:"Archivo Black",Arial,sans-serif;font-size:78px;line-height:1.2;color:var(--white);letter-spacing:1px}
.hero-sub{top:433px;font-size:26px;color:var(--white)}
.btn{position:absolute;display:block;text-align:center;font-family:"Open Sans",Arial,sans-serif;font-weight:600;text-decoration:none;text-transform:uppercase;border-radius:30px}
.btn-red{background:var(--red);color:var(--white)}
.btn-outline{background:var(--white);color:var(--red);border:2px solid var(--red)}
.btn-white{background:var(--white);color:var(--red)}
.dots{top:770px;left:574px;display:flex;gap:8px;align-items:center;z-index:2}
.dots i{display:block;width:12px;height:12px;border-radius:50%;background:var(--white)}
.dots i.on{width:16px;height:16px;background:var(--red);border:3px solid var(--white)}

/* welcome */
.welcome-kicker{left:111px;top:966px;font-family:"Roboto Condensed",Arial,sans-serif;font-size:38px;color:var(--red)}
.welcome-title{left:111px;top:1020px;font-family:"Archivo Black",Arial,sans-serif;font-size:34px;color:var(--grey)}
.welcome-text{left:111px;width:470px;font-size:14px;line-height:27px;color:var(--text)}
.welcome-photo{left:637px;top:972px;width:449px;height:360px;border:5px solid #f26f76;background:linear-gradient(180deg,#e4863a 0%,#b95a2b 35%,#6d6a55 60%,#8a8466 100%)}

/* about band */
.about{top:1400px;left:0;width:1200px;height:873px;background:linear-gradient(180deg,var(--band-top),var(--band-bottom))}
.about-title{top:1610px;font-family:"Roboto Condensed",Arial,sans-serif;font-weight:400;font-size:36px;color:var(--white)}
.about-title b{font-family:"Archivo Black",Arial,sans-serif;font-weight:400}
.rule{height:2px;background:var(--white);width:80px;left:560px}
.about-text{left:155px;width:890px;text-align:center;font-size:16px;line-height:32px;color:#eef0f2}

/* services */
.services-title{top:2306px;font-family:"Roboto Condensed",Arial,sans-serif;font-weight:400;font-size:36px;color:var(--red)}
.services-title b{color:var(--grey)}
.service-card{top:2427px;width:230px;height:320px;border:2px solid var(--card-line);background:var(--white)}
.service-photo{height:154px;border-bottom:1px solid var(--card-line)}
.service-name{position:absolute;left:20px;top:176px;font-family:"Roboto Condensed",Arial,sans-serif;font-weight:700;font-size:15px;letter-spacing:1px;color:var(--ink)}
.service-text{position:absolute;left:20px;top:206px;width:190px;font-size:12px;line-height:18px;color:var(--text)}
.service-link{position:absolute;left:0;top:262px;width:226px;height:54px;border-top:2px solid var(--card-line);padding:18px 0 0 20px;font-size:12px;font-weight:600;color:var(--red);text-decoration:none}

/* footer */
.site-footer{top:2925px;left:0;width:1200px;height:794px;background:var(--footer)}
.footer-brand{top:3090px;font-family:"Roboto Condensed",Arial,sans-serif;font-weight:700;font-size:48px;letter-spacing:2px;color:#aeb3b9;text-transform:uppercase}
.footer-nav{top:3214px;left:0;width:1200px;display:flex;justify-content:center;gap:42px}
.footer-nav a{font-family:"Roboto Condensed",Arial,sans-serif;font-size:14px;color:var(--white);text-decoration:none}
.footer-line{left:111px;width:978px;height:1px;background:var(--footer-line)}
.follow{top:3305px;left:0;width:1200px;display:flex;justify-content:center;align-items:center;gap:12px;font-size:14px;color:var(--white)}
.social{width:34px;height:34px;border:2px solid var(--white);border-radius:50%;display:flex;align-items:center;justify-content:center}
.contact-icon{width:72px;height:72px;border-radius:50%;background:var(--red);display:flex;align-items:center;justify-content:center}
.contact-text{font-size:17px;color:var(--footer-text);text-align:center;width:400px}
.copyright{top:3642px;font-size:13px;color:var(--footer-text)}
</style>
</head>
<body>

<header class="abs site-header">
  <div class="abs brand">Meridel Haulage</div>
  <nav class="main-nav">
    <a class="active" href="#" style="left:617px">HOME</a>
    <a href="#" style="left:713px">ABOUT</a>
    <a href="#" style="left:815px">SERVICES</a>
    <a href="#" style="left:936px">JOBS</a>
    <a href="#" style="left:1027px">CONTACT</a>
  </nav>
</header>

<section class="abs hero" role="img" aria-label="Tractor-trailer hauling white tanks on a flatbed, parked beside bare winter trees"></section>
<svg class="abs" style="top:690px;left:0" width="1200" height="200" viewBox="0 0 1200 200" aria-hidden="true">
  <path d="M0,40 Q600,250 1200,40 L1200,200 L0,200Z" fill="var(--road)"/>
  <path d="M0,88 Q600,298 1200,88 L1200,200 L0,200Z" fill="var(--red)"/>
  <path d="M0,102 Q600,312 1200,102 L1200,200 L0,200Z" fill="var(--white)"/>
</svg>
<h1 class="abs center-x hero-title">MERIDEL HAULAGE</h1>
<p class="abs center-x hero-sub">Excepteur sint occaecat cupidatat non proident, sunt in culpa qui officia</p>
<a class="btn btn-red" href="#" style="left:503px;top:506px;width:194px;height:60px;line-height:60px;font-size:17px">Apply Now</a>
<div class="abs dots"><i></i><i class="on"></i><i></i></div>

<section>
  <div class="abs welcome-kicker">WELCOME TO</div>
  <h2 class="abs welcome-title">MERIDEL HAULAGE</h2>
  <p class="abs welcome-text" style="top:1086px">Nemo enim ipsam voluptatem quia voluptas sit aspernatur aut odit aut fugit, sed quia consequuntur magni dolores eos qui ratione voluptatem sequi nesciu tsquam est, qui dolorem ipsum.</p>
  <p class="abs welcome-text" style="top:1186px">Sed quia non numquam eius modi tempora incidunt ut labore et dolore magnam aliquam quaerat voluptatem.</p>
  <a class="btn btn-outline" href="#" style="left:111px;top:1282px;width:148px;height:50px;line-height:46px;font-size:15px">Read More</a>
  <div class="abs welcome-photo" role="img" aria-label="Pickup truck towing a travel trailer along a desert highway at sunset"></div>
</section>

<section class="abs about" role="img" aria-label="Snowy winter road with evergreen trees under an overcast sky"></section>
<svg class="abs" style="top:1398px;left:0" width="1200" height="120" viewBox="0 0 1200 120" aria-hidden="true">
  <path d="M0,0 L1200,0 L1200,2 Q900,12 600,115 Q300,12 0,2Z" fill="#fff"/>
</svg>
<svg class="abs" style="top:2160px;left:0" width="1200" height="116" viewBox="0 0 1200 116" aria-hidden="true">
  <path d="M0,116 L1200,116 L1200,114 Q900,104 600,0 Q300,104 0,114Z" fill="#fff"/>
</svg>
<h2 class="abs center-x about-title">ABOUT <b>MERIDEL HAULAGE</b></h2>
<div class="abs rule" style="top:1660px"></div>
<p class="abs about-text" style="top:1692px">But I must explain to you how all this mistaken idea of denouncing pleasure and praising pain was born and I will give you a complete account of the system, and expound the actual teachings of the great explorer of the truth, the master-builder of human happiness. No one rejects, dislikes, or avoids pleasure itself, because it is pleasure, but because those who do not know how to pursue pleasure rationally encounter consequences that are extremely painful.</p>
<p class="abs about-text" style="top:1838px">At vero eos et accusamus et iusto odio dignissimos ducimus qui blanditiis praesentium voluptatum deleniti atque corrupti quos dolores et quas molestias excepturi sint occaecati cupiditate non provident, similique sunt in culpa qui officia deserunt mollitia animi, id est laborum et dolorum fuga.</p>
<a class="btn btn-white" href="#" style="left:508px;top:1983px;width:184px;height:60px;line-height:60px;font-size:16px">Learn More</a>

<section>
  <h2 class="abs center-x services-title">OUR <b>SERVICES</b></h2>
  <div class="abs rule" style="top:2355px;background:#9a9a9a"></div>

  <article class="abs service-card" style="left:111px">
    <div class="service-photo" role="img" aria-label="Workers in protective suits beside a large tanker" style="background:linear-gradient(180deg,#8fa584,#6d7a72 60%,#4f8a5a)"></div>
    <h3 class="service-name">VIVAMUS ENIM</h3>
    <p class="service-text">Sunt in culpa qui officia deserunt mollit anim id est laborum</p>
    <a class="service-link" href="#">› Read More</a>
  </article>
  <article class="abs service-card" style="left:360px">
    <div class="service-photo" role="img" aria-label="White semi-trucks parked in a yard" style="background:linear-gradient(180deg,#a9b4bd,#8b8f93 55%,#6f5e50)"></div>
    <h3 class="service-name">EGET TINCI</h3>
    <p class="service-text">Sunt in culpa qui officia deserunt mollit anim id est laborum</p>
    <a class="service-link" href="#">› Read More</a>
  </article>
  <article class="abs service-card" style="left:609px">
    <div class="service-photo" role="img" aria-label="Forklift loading cargo onto a flatbed trailer" style="background:linear-gradient(180deg,#8d8e84,#6e6b60 55%,#9a8e72)"></div>
    <h3 class="service-name">TORTOR EGET</h3>
    <p class="service-text">Sunt in culpa qui officia deserunt mollit anim id est laborum</p>
    <a class="service-link" href="#">› Read More</a>
  </article>
  <article class="abs service-card" style="left:858px">
    <div class="service-photo" role="img" aria-label="Rear view of a tanker truck on the highway" style="background:linear-gradient(180deg,#9aa2a8,#7c7472 50%,#8a3a38)"></div>
    <h3 class="service-name">ALIQUAM MOLESTIE</h3>
    <p class="service-text">Sunt in culpa qui officia deserunt mollit anim id est laborum</p>
    <a class="service-link" href="#">› Read More</a>
  </article>

  <a class="btn btn-red" href="#" style="left:503px;top:2821px;width:194px;height:60px;line-height:60px;font-size:17px">View More</a>
</section>

<footer class="abs site-footer" role="img" aria-label="Dark, dimly lit road scene behind the footer"></footer>
<svg class="abs" style="top:2918px;left:0" width="1200" height="100" viewBox="0 0 1200 100" aria-hidden="true">
  <path d="M0,0 L1200,0 L1200,8 Q600,110 0,8Z" fill="#fff"/>
  <path d="M0,14 Q600,116 1200,14" fill="none" stroke="var(--red)" stroke-width="12"/>
</svg>
<div class="abs center-x footer-brand">Meridel Haulage</div>
<nav class="abs footer-nav">
  <a href="#">HOME</a><a href="#">ABOUT</a><a href="#">SERVICES</a><a href="#">JOBS</a><a href="#">CONTACT</a>
</nav>
<div class="abs footer-line" style="top:3262px"></div>
<div class="abs follow">
  <span>Follow Meridel Haulage:</span>
  <a class="social" href="#" aria-label="Message us">
    <svg width="16" height="16" viewBox="0 0 24 24" aria-hidden="true"><path fill="#fff" d="M3 4h18v12H8l-5 4z"/></svg>
  </a>
  <a class="social" href="#" aria-label="Share">
    <svg width="16" height="16" viewBox="0 0 24 24" aria-hidden="true"><circle cx="18" cy="5" r="3" fill="#fff"/><circle cx="6" cy="12" r="3" fill="#fff"/><circle cx="18" cy="19" r="3" fill="#fff"/><path d="M18 5L6 12l12 7" fill="none" stroke="#fff" stroke-width="2"/></svg>
  </a>
  <a class="social" href="#" aria-label="Job listings">
    <svg width="16" height="16" viewBox="0 0 24 24" aria-hidden="true"><path fill="#fff" d="M9 3h6v3h6v14H3V6h6zm2 2v1h2V5z"/></svg>
  </a>
</div>
<div class="abs footer-line" style="top:3384px"></div>
<div class="abs" style="left:600px;top:3410px;width:1px;height:160px;background:var(--footer-line)"></div>

<div class="abs contact-icon" style="left:380px;top:3435px">
  <svg width="30" height="30" viewBox="0 0 24 24" aria-hidden="true"><path fill="#fff" d="M6.6 10.8a15.1 15.1 0 0 0 6.6 6.6l2.2-2.2a1 1 0 0 1 1-.25 11.4 11.4 0 0 0 3.6.57 1 1 0 0 1 1 1V20a1 1 0 0 1-1 1A17 17 0 0 1 3 4a1 1 0 0 1 1-1h3.5a1 1 0 0 1 1 1c0 1.25.2 2.45.57 3.57a1 1 0 0 1-.25 1z"/></svg>
</div>
<div class="abs contact-icon" style="left:765px;top:3435px">
  <svg width="30" height="30" viewBox="0 0 24 24" aria-hidden="true"><path fill="#fff" d="M2 5h20v14H2z"/><path d="M2 5l10 8 10-8" fill="none" stroke="var(--red)" stroke-width="2"/></svg>
</div>
<p class="abs contact-text" style="left:216px;top:3518px">Phone: +1 (555) 014-2277</p>
<p class="abs contact-text" style="left:601px;top:3518px">Email: info@meridelhaulage.com</p>
<p class="abs center-x copyright">Copyrights © 2019 Meridel Haulage. All rights reserved.</p>

</body>
</html>
```